Business Card Design

i need a business card to promote my Handyman & Gardening business. It would be nice to see a design incorporating both of these things. We are happy to help in any way we can with no job ever being to small.

Industry/Entity Type

Business

Contact Information for Business Card

Dave's Handyman & Gardening Service
Dave Holt
PO Box 312 Fernby SA 5499
dave.holt@fernmail.com
ph 0412 736 508

```html
<!DOCTYPE html>
<html lang="en">
<head>
<meta charset="UTF-8">
<title>Dave's Handyman &amp; Gardening Service – Business Card</title>
<link href="https://fonts.googleapis.com/css2?family=Open+Sans:wght@400;600;700&display=swap" rel="stylesheet">
<style>
  :root {
    --backdrop: #4d5655;
    --card: #f6f8f8;
    --orange: #ff8c00;
    --ink: #3a3a3a;
    --white: #ffffff;
  }
  * { margin: 0; padding: 0; box-sizing: border-box; }
  html, body {
    width: 1200px; height: 960px; overflow: hidden;
    background: var(--backdrop);
    font-family: "Open Sans", Arial, sans-serif;
  }
  .business-card {
    position: absolute; left: 97px; top: 157px;
    width: 1012px; height: 624px;
    background: radial-gradient(ellipse at 50% 40%, var(--white) 0%, var(--card) 70%, #eef1f3 100%);
  }
  .brand-mark {
    position: absolute; left: 0; right: 0; top: 130px;
    display: flex; justify-content: center; align-items: center; gap: 14px;
    color: var(--orange); font-weight: 700; font-size: 40px;
  }
  .brand-mark .dot {
    width: 22px; height: 22px; border-radius: 50%; background: var(--orange);
  }
  .title-band {
    position: absolute; left: 0; top: 281px; width: 100%; height: 78px;
    background: var(--orange);
    display: flex; align-items: center; justify-content: center;
    color: var(--white); font-weight: 700; font-size: 26px;
  }
  .owner-name {
    position: absolute; left: 378px; top: 383px;
    display: flex; align-items: center; gap: 4px;
    color: var(--ink); font-size: 38px; font-weight: 400;
  }
  .owner-name svg { width: 26px; height: 40px; }
  .contact-row {
    position: absolute; top: 532px; height: 32px;
    display: flex; align-items: center; gap: 8px;
    color: var(--ink); font-size: 21px; font-weight: 400;
  }
  .contact-row svg { flex: none; }
  .contact-email { left: 46px; }
  .contact-phone { left: 412px; }
  .contact-address { left: 680px; }
</style>
</head>
<body>
<main class="business-card">
  <div class="brand-mark"><span class="dot"></span>Dave's</div>

  <div class="title-band">Dave's Handyman &amp; Gardening Service</div>

  <div class="owner-name">
    <svg viewBox="0 0 26 40" aria-hidden="true">
      <circle cx="13" cy="9" r="6" fill="var(--orange)"/>
      <path d="M3 18 Q13 14 23 18 L23 38 L3 38 Z" fill="var(--orange)"/>
      <path d="M13 18 L11 26 L13 32 L15 26 Z" fill="var(--white)"/>
    </svg>
    <span>Dave Holt</span>
  </div>

  <div class="contact-row contact-email">
    <svg width="34" height="24" viewBox="0 0 34 24" aria-hidden="true">
      <rect x="0" y="0" width="34" height="24" fill="var(--orange)"/>
      <path d="M1 1 L17 14 L33 1" fill="none" stroke="var(--white)" stroke-width="2"/>
      <path d="M1 23 L13 11 M33 23 L21 11" stroke="var(--white)" stroke-width="2"/>
    </svg>
    <span>dave.holt@fernmail.com</span>
  </div>

  <div class="contact-row contact-phone">
    <svg width="28" height="28" viewBox="0 0 28 28" aria-hidden="true">
      <circle cx="14" cy="14" r="12" fill="none" stroke="var(--orange)" stroke-width="2.5"/>
      <path d="M9 8 L12 8 L13 11 L11 13 Q13 16 15 17 L17 15 L20 16 L20 19 Q18 21 15 20 Q9 17 8 11 Q8 9 9 8 Z" fill="var(--orange)"/>
    </svg>
    <span>0412 736 508</span>
  </div>

  <div class="contact-row contact-address">
    <svg width="26" height="28" viewBox="0 0 26 28" aria-hidden="true">
      <rect x="2" y="2" width="5" height="10" fill="var(--orange)"/>
      <path d="M0 28 L0 12 L8 7 L8 12 L16 7 L16 12 L26 6 L26 28 Z" fill="var(--orange)"/>
    </svg>
    <span>PO Box 312 , Fernby SA 5499</span>
  </div>
</main>
</body>
</html>
```